Dental care for hole family, announcement in newspaper

Hey! I have Dental surgery Business in middle of Finland in Jyväskylä. You can see my web www.hammasvelmora.fi.
Now I am looking for new way to do advertisement, more visual I hope.
I woul like to have announcement in newspaper. I would like to tell that we treating hole family from babyes to seniors. I saw here in your pages cute photo where about 1-year old baby was brushing teeth ja looking with big eys to me. It is the feeling I am looking for. My idea is to tell people, that in our klinik, they can have "own dental hygienist" who is taking care of them with dentists of different spesialitis.
Now I need advertisements for that information!!

Yours, Velmora

Target Market(s)

All.

Industry/Entity Type

Dental Clinic

Requirements
Must have
• Visual components, whicts are matching with my homepages visual look (www.hammasvelmora.fi).
Nice to have
• My logo, whitch you can find from my webpages.

```html
<!DOCTYPE html>
<html lang="en">
<head>
<meta charset="utf-8">
<title>Hammasvelmora – Dental care for the whole family</title>
<link rel="stylesheet" href="https://fonts.googleapis.com/css2?family=Comfortaa:wght@500&family=Raleway:wght@300;400;500;700&family=Tinos:wght@400;700&display=swap">
<style>
  :root {
    --page-bg: #e6e7e9;
    --paper: #ffffff;
    --brown-dark: #5a2f12;
    --brown-band: #7f5034;
    --brown-text: #5b3a22;
    --sky: #2ea3d9;
    --lime: #a8c23a;
    --lime-soft: #cfe196;
    --headline-edge: #5c6b2a;
    --yellow: #f2e94a;
    --ink: #222222;
    --white: #ffffff;
    --accent-dot: #f5a623;
  }
  * { box-sizing: border-box; margin: 0; padding: 0; }
  html, body { width: 1200px; height: 1200px; overflow: hidden; background: var(--page-bg); }
  .flyer {
    position: absolute; left: 194px; top: 46px; width: 812px; height: 1081px;
    background: var(--paper); overflow: hidden; font-family: "Raleway", sans-serif;
  }
  .hero-photo {
    position: absolute; left: 430px; top: 0; width: 382px; height: 532px;
    background: radial-gradient(ellipse at 62% 42%, #f6cdb1 0%, #f3d6c3 35%, #f8ece4 62%, #ffffff 85%);
  }
  .brand { position: absolute; top: 26px; right: 374px; text-align: right; color: var(--brown-text); }
  .brand-kind { font-size: 15px; letter-spacing: 0.5px; }
  .brand-name { font-size: 29px; font-weight: 500; letter-spacing: 1px; line-height: 1.1; }
  .brand-partner { display: inline-block; width: 9px; height: 9px; border-radius: 50%; background: var(--accent-dot); margin-top: 2px; }
  .headline {
    position: absolute; top: 98px; right: 356px; width: 460px; text-align: right;
    font-family: "Comfortaa", sans-serif; font-weight: 500; font-size: 45px; line-height: 56px;
    color: var(--lime-soft); -webkit-text-stroke: 1.2px var(--headline-edge); letter-spacing: -0.5px;
  }
  .welcome {
    position: absolute; left: 27px; top: 296px; width: 252px; height: 236px;
    background: var(--brown-dark); color: var(--white); font-family: "Tinos", serif; padding: 20px 0 0 10px;
  }
  .welcome-title { font-size: 45px; line-height: 1; margin-bottom: 30px; }
  .welcome-text { font-size: 24px; line-height: 32px; }
  .welcome-text strong { display: block; font-size: 32px; margin-top: 6px; }
  .booking { position: absolute; left: 306px; top: 374px; color: var(--ink); }
  .booking-call { font-size: 32px; font-weight: 300; }
  .booking-call b { color: var(--lime); font-weight: 700; }
  .booking-line { font-size: 33px; font-weight: 300; margin-top: 4px; white-space: nowrap; }
  .booking-phone { font-size: 34px; font-weight: 700; color: var(--lime); margin-top: 4px; }
  .stripe { position: absolute; left: 0; top: 532px; width: 812px; height: 22px; background: var(--sky); }
  .info {
    position: absolute; left: 0; top: 554px; width: 812px; height: 527px;
    background: linear-gradient(90deg, var(--brown-band) 0%, var(--brown-band) 45%, #8d5d40 75%, #9b6a4c 100%);
    color: var(--white);
  }
  .column { position: absolute; top: 25px; width: 240px; text-align: center; }
  .col-about { left: 28px; }
  .col-practice { left: 284px; }
  .col-events { left: 540px; }
  .icon-ring { display: block; margin: 0 auto; width: 120px; height: 120px; }
  .column h2 { font-size: 25px; font-weight: 700; line-height: 32px; margin-top: 28px; }
  .column p { font-size: 18px; font-weight: 300; line-height: 23px; margin-top: 12px; }
  .col-events p { margin-top: 0; }
  .column p strong { font-weight: 700; }
  .call-now { position: absolute; left: 531px; top: 354px; width: 254px; text-align: center; }
  .call-now-title { font-size: 42px; font-weight: 700; }
  .call-now-phone {
    margin-top: 6px; height: 46px; background: var(--lime);
    font-size: 33px; font-weight: 400; line-height: 46px; color: var(--white);
  }
  .visit { position: absolute; left: 28px; top: 460px; font-size: 33px; font-weight: 700; }
</style>
</head>
<body>
<main class="flyer">
  <div class="hero-photo" role="img" aria-label="Photo of a baby with big blue eyes holding a green toothbrush"></div>

  <div class="brand">
    <div class="brand-kind">Hammaslääkäriasema</div>
    <div class="brand-name">HAMMASVELMORA</div>
    <span class="brand-partner"></span>
  </div>

  <h1 class="headline">We treating hole family from babyes to seniors</h1>

  <section class="welcome">
    <div class="welcome-title">WELCOME</div>
    <p class="welcome-text">Let us show what we can do for your <strong>dental health</strong></p>
  </section>

  <div class="booking">
    <div class="booking-call"><b>CALL</b> &amp;</div>
    <div class="booking-line">BOOK YOUR APPOINTMENT</div>
    <div class="booking-phone">014 555 0192</div>
  </div>

  <div class="stripe"></div>

  <section class="info">
    <div class="column col-about">
      <svg class="icon-ring" viewBox="0 0 120 120" aria-hidden="true">
        <circle cx="60" cy="60" r="57" fill="none" stroke="#ffffff" stroke-width="2.5"/>
        <circle cx="60" cy="42" r="14" fill="#ffffff"/>
        <path d="M34 86 q0-24 26-24 q26 0 26 24 z" fill="#ffffff"/>
        <path d="M48 64 v10 a6 6 0 0 0 12 0" fill="none" stroke="#7f5034" stroke-width="3"/>
        <circle cx="72" cy="76" r="4" fill="none" stroke="#7f5034" stroke-width="3"/>
      </svg>
      <h2>About Us</h2>
      <p>Dental Velmora is in Jyväskylä, Saarijärvi Located dental clinic that offers high-quality private dental treatment. Our reception belong to the national CarePlus Group.</p>
    </div>
    <div class="column col-practice">
      <svg class="icon-ring" viewBox="0 0 120 120" aria-hidden="true">
        <circle cx="60" cy="60" r="57" fill="none" stroke="#f2e94a" stroke-width="2.5"/>
        <rect x="48" y="34" width="24" height="12" rx="3" fill="none" stroke="#f2e94a" stroke-width="5"/>
        <rect x="30" y="44" width="60" height="42" rx="5" fill="#f2e94a"/>
        <rect x="55" y="52" width="10" height="26" fill="#7f5034"/>
        <rect x="47" y="60" width="26" height="10" fill="#7f5034"/>
      </svg>
      <h2>Dental Practice</h2>
      <p>Esthetic dentistry, Scaling, dental care of the elderly, root canal treatments, imaging, <strong>Children's dental care,</strong> Oral surgery, orthodontics and more. please visit our website.</p>
    </div>
    <div class="column col-events">
      <svg class="icon-ring" viewBox="0 0 120 120" aria-hidden="true">
        <circle cx="60" cy="60" r="57" fill="none" stroke="#a8c23a" stroke-width="2.5"/>
        <circle cx="60" cy="60" r="27" fill="none" stroke="#a8c23a" stroke-width="8"/>
        <path d="M58 46 v17 h12" fill="none" stroke="#a8c23a" stroke-width="6"/>
      </svg>
      <h2>Hammasvelmoran events</h2>
      <p>Come and explore new at reception - Win your teeth soodapuhdistus! <strong>Hammasvelmoran events</strong></p>
    </div>

    <div class="call-now">
      <div class="call-now-title">Call Now</div>
      <div class="call-now-phone">014 555 0192</div>
    </div>

    <div class="visit">Visit : www.hammasvelmora.fi</div>
  </section>
</main>
</body>
</html>
```